Thai Restruant Business Card Design

A Business card design for a Thai and Laos take away restaurant.

We are a highly respectable take away restaurant in a small shopping center.

The design must have a Papaya Tree and Thai Palace.

The final design should communicate, innovation, fun and delicious food.

Industry/Entity Type

Restaurant

Contact Information for Business Card

Mango Hearth, Thai & Lao Food, Shop 4. 17 Elmsworth Lane. Cabramatta N.S.W 2166, Tel. 02-96417725, Open 7 Days From 8.30am To 6.30pm

```html
<!DOCTYPE html>
<html lang="en">
<head>
<meta charset="utf-8">
<title>Mango Hearth – Business Card</title>
<link rel="stylesheet" href="https://fonts.googleapis.com/css2?family=Oswald:wght@400;500&family=UnifrakturMaguntia&display=swap">
<style>
  :root {
    --card-red: #ff0000;
    --band-red: #990000;
    --ink: #111111;
    --hours-text: #ff1f1f;
    --art-dark: #2a0000;
    --art-glow: #d80000;
  }
  html, body {
    margin: 0;
    padding: 0;
    overflow: hidden;
    background: var(--card-red);
  }
  .card {
    position: relative;
    width: 1200px;
    height: 741px;
    background: var(--card-red);
    overflow: hidden;
  }
  .phone {
    position: absolute;
    top: 12px;
    right: 14px;
    margin: 0;
    font-family: "Oswald", sans-serif;
    font-weight: 500;
    font-size: 58px;
    line-height: 1;
    letter-spacing: 1px;
    color: var(--ink);
    transform: scaleX(0.82);
    transform-origin: right top;
    white-space: nowrap;
  }
  .hero-art {
    position: absolute;
    left: 346px;
    top: 92px;
    width: 489px;
    height: 157px;
    background: radial-gradient(ellipse at 50% 100%, var(--art-glow) 0%, var(--art-dark) 70%);
  }
  .brand-name {
    position: absolute;
    left: 0;
    width: 1200px;
    top: 274px;
    margin: 0;
    text-align: center;
    font-family: "Oswald", sans-serif;
    font-weight: 500;
    font-size: 70px;
    line-height: 1;
    letter-spacing: 1px;
    color: var(--ink);
    white-space: nowrap;
  }
  .cuisine {
    position: absolute;
    left: 0;
    width: 1200px;
    top: 386px;
    margin: 0;
    text-align: center;
    font-family: "UnifrakturMaguntia", serif;
    font-weight: 400;
    font-size: 94px;
    line-height: 100px;
    color: var(--ink);
    white-space: nowrap;
  }
  .hours-band {
    position: absolute;
    left: 274px;
    top: 496px;
    width: 652px;
    height: 91px;
    background: var(--band-red);
    display: flex;
    align-items: center;
    justify-content: center;
  }
  .hours {
    margin: 0;
    font-family: "Oswald", sans-serif;
    font-weight: 400;
    font-size: 38px;
    line-height: 1;
    color: var(--hours-text);
    transform: scaleX(0.8);
    white-space: nowrap;
  }
  .address {
    position: absolute;
    left: 0;
    width: 1200px;
    top: 680px;
    margin: 0;
    text-align: center;
    font-family: "Oswald", sans-serif;
    font-weight: 500;
    font-size: 40px;
    line-height: 1;
    letter-spacing: 1px;
    color: var(--ink);
    transform: scaleX(0.82);
    white-space: nowrap;
  }
</style>
</head>
<body>
  <main class="card">
    <p class="phone">Tel. 02-96417725</p>

    <div class="hero-art" role="img" aria-label="Silhouette illustration of a Thai palace between papaya palm trees against a setting sun"></div>

    <h1 class="brand-name">Mango Hearth</h1>

    <h2 class="cuisine">Thai &amp; Lao Food</h2>

    <div class="hours-band">
      <p class="hours">Open 7 Days From 8.30am To 6.30pm</p>
    </div>

    <p class="address">Shop 4. 17 Elmsworth Lane. Cabramatta N.S.W 2166</p>
  </main>
</body>
</html>
```